Business card design needed

My business is in Matchmaking. My objective is to find the most compatible partner for my clients....basically I'm in the love and happiness industry bringing two people together for a lasting loving relationship.

I envision the design to be something with 2 people who are in love looking happy or even a silhouette.....I don't really know, I'm open to ideas.....maybe no picture at all, but I want it to be classy :-)

I do have a logo which I will upload. You can also go to my website to give you an idea on the colours and the design if that helps, however the website is not finished yet, it should be up by today or tomorrow. If the website has a heart with swirls on the upper left hand corner, that is the old website, please ignore that one. The one that will be up shortly has a picture frame on the home page with my logo that will be in the file I will upload on this page.

Target Market(s)

There are three categories: Over 45, Asian and Western and same sex, but would be able to afford to hire a matchmaker

Industry/Entity Type

Industry

Contact Information for Business Card

The Tidewell Bureau
Helping You Find The "One"
Maris Pelloway
Matchmaker
0491 572 064
info@tidewellbureau.com.au
www.tidewellbureau.com.au

```html
<!DOCTYPE html>
<html lang="en">
<head>
<meta charset="utf-8">
<title>The Tidewell Bureau – Business Card</title>
<link rel="stylesheet" href="https://fonts.googleapis.com/css2?family=Great+Vibes&family=Lato:wght@400&display=swap">
<style>
  :root {
    --canvas-bg: #e9e4dc;
    --card-black: #15171a;
    --card-black-edge: #24272b;
    --band-orange: #c4531f;
    --band-orange-dark: #a8421a;
    --name-grey: #d9dcdd;
    --photo-light: #efe6d8;
    --photo-mid: #b9a58a;
    --photo-dark: #5c4a38;
    --email-ink: #f4efe6;
  }
  * { box-sizing: border-box; margin: 0; padding: 0; }
  html, body { width: 921px; height: 1200px; overflow: hidden; }
  body {
    background: var(--canvas-bg);
    display: flex;
    flex-direction: column;
    align-items: center;
    justify-content: center;
    gap: 110px;
  }
  .card {
    position: relative;
    width: 700px;
    height: 400px;
    overflow: hidden;
    box-shadow: 0 10px 28px rgba(0,0,0,0.25);
  }
  .band {
    position: absolute;
    top: 0;
    bottom: 0;
    width: 78px;
    background: linear-gradient(90deg, var(--band-orange-dark), var(--band-orange) 40%, var(--band-orange-dark));
  }
  .band--left { left: 0; }
  .band--right { right: 0; }

  /* Front */
  .card--front {
    background: linear-gradient(160deg, var(--card-black-edge), var(--card-black) 55%);
  }
  .front-brand {
    position: absolute;
    left: 78px;
    right: 78px;
    top: 0;
    bottom: 0;
    display: flex;
    flex-direction: column;
    align-items: center;
    justify-content: center;
    gap: 22px;
  }
  .brand-dot {
    width: 62px;
    height: 62px;
    border-radius: 50%;
    background: var(--name-grey);
    opacity: 0.85;
  }
  .brand-name {
    font-family: "Great Vibes", cursive;
    font-size: 58px;
    font-weight: 400;
    color: var(--name-grey);
    line-height: 1;
  }

  /* Back */
  .card--back { background: var(--photo-mid); }
  .couple-photo {
    position: absolute;
    left: 78px;
    right: 78px;
    top: 0;
    bottom: 0;
    background: radial-gradient(ellipse at 65% 35%, var(--photo-dark) 0%, var(--photo-mid) 45%, var(--photo-light) 100%);
  }
  .back-brand {
    position: absolute;
    left: 104px;
    bottom: 78px;
    font-family: "Great Vibes", cursive;
    font-size: 40px;
    color: var(--name-grey);
    line-height: 1;
  }
  .back-email {
    position: absolute;
    left: 104px;
    bottom: 30px;
    font-family: "Lato", sans-serif;
    font-size: 16px;
    letter-spacing: 0.5px;
    color: var(--email-ink);
  }
</style>
</head>
<body>
  <section class="card card--front">
    <div class="band band--left"></div>
    <div class="front-brand">
      <div class="brand-dot"></div>
      <h1 class="brand-name">The Tidewell Bureau</h1>
    </div>
    <div class="band band--right"></div>
  </section>

  <section class="card card--back">
    <div class="band band--left"></div>
    <div class="couple-photo" role="img" aria-label="Sepia photograph of a smiling couple embracing outdoors"></div>
    <p class="back-brand">The Tidewell Bureau</p>
    <p class="back-email">info@tidewellbureau.com.au</p>
    <div class="band band--right"></div>
  </section>
</body>
</html>
```